Package Design for Chew Bone Guild for Rivora

Would like a label to put on a 6x9 package.

Here is my site: chewboneguild.example

Here are the labels I like:
https://tomandhound.example/collections/chews/products/6-inch-basic-chews
https://www.rivora.example/stores/Tom+%26+Hound/page/A1D23456-7ABC-42EF-9D01-123456789ABC?ref_=xyz_qrs
https://quiet-meadowland.example/amber-paw-mini-chews-6-25-pack/
https://www.fernandkettle.example/shop/open-trail-chew-rods

```html
<!DOCTYPE html>
<html lang="en">
<head>
<meta charset="utf-8">
<title>Chew Bone Guild – Premium Chews Pouch</title>
<link rel="stylesheet" href="https://fonts.googleapis.com/css2?family=Lilita+One&family=Oswald:wght@500&family=Montserrat:wght@600;800&display=swap">
<style>
  :root {
    --backdrop: #e4e4e6;
    --kraft: #b7a690;
    --kraft-deep: #a69580;
    --ink: #2b2724;
    --cream: #f4f1ec;
    --strip: #c9b9a3;
    --chew-dark: #4a2414;
    --chew-mid: #8a3f1e;
    --chew-light: #c87a4c;
  }
  * { margin: 0; padding: 0; box-sizing: border-box; }
  html, body { width: 1200px; height: 835px; overflow: hidden; background: var(--backdrop); }
  .stage { position: relative; width: 1200px; height: 835px; }
  .pouch { position: absolute; left: 350px; top: 28px; width: 500px; height: 780px; }
  .brand-name { font-family: "Montserrat", sans-serif; font-weight: 800; font-size: 11px; fill: var(--ink); letter-spacing: 0.5px; }
  .headline { font-family: "Lilita One", sans-serif; font-size: 46px; fill: var(--ink); letter-spacing: 1px; }
  .product-title { font-family: "Oswald", sans-serif; font-weight: 500; font-size: 56px; fill: var(--cream); }
  .size-mark { font-family: "Oswald", sans-serif; font-weight: 500; font-size: 70px; fill: var(--cream); }
  .claim { font-family: "Oswald", sans-serif; font-weight: 500; font-size: 22px; fill: var(--ink); }
  .sub-title { font-family: "Montserrat", sans-serif; font-weight: 800; font-size: 27px; fill: var(--cream); letter-spacing: 0.5px; }
  .benefit-label { font-family: "Montserrat", sans-serif; font-weight: 600; font-size: 5.5px; fill: var(--cream); }
</style>
</head>
<body>
<main class="stage">
  <svg class="pouch" viewBox="0 0 500 780" xmlns="http://www.w3.org/2000/svg">
    <defs>
      <linearGradient id="chew-fill" x1="0" x2="1" y1="0" y2="0">
        <stop offset="0" stop-color="var(--chew-dark)"/>
        <stop offset="0.2" stop-color="var(--chew-light)"/>
        <stop offset="0.35" stop-color="var(--chew-dark)"/>
        <stop offset="0.5" stop-color="var(--chew-light)"/>
        <stop offset="0.65" stop-color="var(--chew-mid)"/>
        <stop offset="0.8" stop-color="var(--chew-light)"/>
        <stop offset="1" stop-color="var(--chew-dark)"/>
      </linearGradient>
      <path id="headline-arc" d="M 60 365 Q 247 300 434 365"/>
    </defs>

    <!-- pouch body -->
    <path class="pouch-body" d="M 14 0 H 486 Q 500 0 500 14 V 780 H 0 V 14 Q 0 0 14 0 Z" fill="var(--kraft)"/>
    <line class="zip-line" x1="0" y1="104" x2="500" y2="104" stroke="var(--kraft-deep)" stroke-width="2"/>
    <path class="tear-notch" d="M 0 56 l 4 3 l -4 3 Z M 500 56 l -4 3 l 4 3 Z" fill="var(--backdrop)"/>

    <!-- brand tab -->
    <rect class="brand-tab" x="42" y="0" width="101" height="84" fill="var(--ink)"/>
    <g class="brand-seal">
      <circle cx="94" cy="129" r="59" fill="var(--cream)" stroke="var(--ink)" stroke-width="3"/>
      <circle cx="94" cy="112" r="9" fill="var(--ink)"/>
      <text class="brand-name" x="94" y="140" text-anchor="middle">CHEW BONE</text>
      <text class="brand-name" x="94" y="154" text-anchor="middle">GUILD</text>
    </g>

    <!-- dog silhouette area -->
    <rect class="mascot" x="167" y="101" width="167" height="170" rx="30" fill="var(--ink)" opacity="0.9"
          role="img" aria-label="Black silhouette of a sitting dog in profile"/>

    <!-- headline -->
    <text class="headline" text-anchor="middle"><textPath href="#headline-arc" startOffset="50%">PREMIUM</textPath></text>

    <!-- product window -->
    <rect class="product-window" x="94" y="494" width="310" height="212" fill="url(#chew-fill)"
          role="img" aria-label="Window showing a row of dried bully sticks"/>

    <!-- title plaque -->
    <path class="title-plaque" d="M 90 400 Q 90 365 130 362 Q 248 350 366 362 Q 407 365 407 400 V 502 Q 407 532 366 535 Q 248 546 130 535 Q 90 532 90 502 Z" fill="var(--ink)"/>
    <path class="title-plaque-rule" d="M 100 404 Q 100 374 134 371 Q 248 360 362 371 Q 397 374 397 404 V 498 Q 397 524 362 527 Q 248 537 134 527 Q 100 524 100 498 Z" fill="none" stroke="var(--cream)" stroke-width="2"/>
    <text class="product-title" x="248" y="472" text-anchor="middle">BULLY STICKS</text>

    <!-- size band -->
    <rect class="size-band" x="94" y="647" width="306" height="101" fill="var(--ink)"/>
    <rect class="claim-strip" x="167" y="651" width="219" height="35" fill="var(--strip)"/>
    <text class="claim" x="276" y="676" text-anchor="middle">NATURALLY ODIUR FREE</text>
    <text class="size-mark" x="100" y="734">6”</text>
    <text class="sub-title" x="276" y="724" text-anchor="middle">BULLY STICKS</text>

    <!-- benefits -->
    <g class="benefits">
      <circle cx="198" cy="752" r="14" fill="var(--cream)"/>
      <circle cx="254" cy="752" r="14" fill="var(--cream)"/>
      <circle cx="310" cy="752" r="14" fill="var(--cream)"/>
      <circle cx="365" cy="752" r="14" fill="var(--cream)"/>
      <text class="benefit-label" x="198" y="773" text-anchor="middle">PREMIUM GRADE</text>
      <text class="benefit-label" x="254" y="773" text-anchor="middle">DENTAL HEALTH</text>
      <text class="benefit-label" x="310" y="773" text-anchor="middle">GRASS FED BEEF</text>
      <text class="benefit-label" x="365" y="773" text-anchor="middle">100% DIGESTIBLE</text>
    </g>
  </svg>
</main>
</body>
</html>
```